https://www.kreidetafel.de - a website for school website in germany for presentation/paper download

we own the webpage https://www.kreidetafel.de and we need a new webdesign (a new website logo is also possible). we want only new images and css, we don´t want to made any change to the HTML code.
we need only new images/color for a new modern look.

we want to have more trust to our user. they have to download presentation/paper
we need template for this sites:
https://www.kreidetafel.de/
https://www.kreidetafel.de/referate/englisch
https://www.kreidetafel.de/forum.php
https://www.kreidetafel.de/forum/insektenhotel/147503
https://www.kreidetafel.de/referat/latein/sokrates/14781
https://www.kreidetafel.de/schule_seminararbeit_fachliste.php?fach=127
and other sites on the website. (take a look around the website)

we don´t like white color for sublines or text. (h1/h2/strong) . in image are white Text OK.

important: we want to chance ONLY the CSS and PICS, we don´t want to remove or chance any HTML code.

after you have made a mockup of the new design and we give you a go, you have to made a package with the IMAGES and the CSS rules (text how we have to chance the current css)

Target Market(s)

Germany, Austria, Switzerland -DACH

Industry/Entity Type

School

Coding

Coded - Design and coding required

Number of Pages Required

5+ page

Font styles to use
Serif
Sans Serif

Colors

Designer to choose colors to be used in the design.

Requirements
Must have
• We want only to remove images and no HTML Code
Should not have
• NO white colors for Text on the site. In images are OK

```html
<!DOCTYPE html>
<html lang="de">
<head>
<meta charset="utf-8">
<title>Kreidetafel.de – Referate, Hausarbeiten, Hausaufgaben</title>
<link href="https://fonts.googleapis.com/css2?family=Poppins:wght@300;400;500;600&display=swap" rel="stylesheet">
<style>
  :root {
    --green: #55b391;
    --green-dark: #2d6b58;
    --green-deep: #245c4b;
    --mint: #e8f8f2;
    --mint-border: #bfe9db;
    --ink: #2f4842;
    --ink-soft: #4a5f5a;
    --link: #3a6aa0;
    --line: #dde5e2;
    --muted: #a4adab;
    --page: #f3f5f5;
  }
  * { box-sizing: border-box; margin: 0; padding: 0; }
  html, body { width: 1200px; height: 1080px; overflow: hidden; }
  body { background: var(--page); font-family: "Poppins", sans-serif; color: var(--ink); }
  a { color: inherit; text-decoration: none; }
  .page { position: relative; width: 960px; height: 1080px; margin: 0 auto; background: #fff; }
  .abs { position: absolute; }

  .brand { left: 20px; top: 38px; font-size: 31px; font-weight: 600; color: var(--green); letter-spacing: .2px; }
  .field { top: 39px; width: 145px; height: 43px; border: 1px solid var(--line); display: flex; align-items: center; gap: 8px; padding-left: 13px; font-size: 12px; color: #8a9b97; }
  .field svg { width: 12px; height: 12px; fill: #a9b5b2; }
  .btn { background: var(--green); color: #fff; font-weight: 500; display: flex; align-items: center; justify-content: center; }
  .login { left: 863px; top: 39px; width: 76px; height: 43px; font-size: 14px; }

  .mainnav { left: 20px; right: 20px; top: 102px; height: 54px; border-top: 1px solid var(--line); display: flex; align-items: center; font-size: 13.5px; letter-spacing: .3px; color: var(--ink); }
  .mainnav a { display: flex; align-items: center; gap: 8px; }
  .mainnav svg { width: 11px; height: 11px; fill: var(--ink); }
  .crumbs { left: 19px; top: 155px; width: 922px; height: 42px; background: #f0fbf7; border: 1px solid var(--mint-border); display: flex; align-items: center; padding-left: 15px; font-size: 14px; color: var(--ink); }
  .crumbs i { color: var(--mint-border); font-style: normal; margin: 0 5px; }

  .side { left: 20px; width: 180px; }
  .side h3 { display: flex; align-items: center; gap: 9px; font-size: 16px; font-weight: 400; color: var(--green); height: 24px; }
  .side h3 svg, .menu svg { width: 12px; height: 12px; fill: var(--green); }
  .menu li { list-style: none; height: 37px; display: flex; align-items: center; gap: 9px; font-size: 14px; border-bottom: 1px solid var(--line); padding-left: 1px; }
  .menu svg { fill: var(--ink); width: 11px; height: 11px; }
  .menu li:last-child { border-bottom: none; }
  .stats li { list-style: none; height: 37px; display: flex; align-items: center; justify-content: space-between; font-size: 14px; border-bottom: 1px solid var(--line); padding-right: 4px; }
  .stats li:last-child { border-bottom: none; }

  .newbox { left: 19px; top: 827px; width: 182px; height: 182px; border: 1px solid var(--line); text-align: center; }
  .newbox h4 { margin-top: 22px; font-size: 14px; font-weight: 400; color: var(--green); display: flex; justify-content: center; gap: 8px; align-items: center; }
  .newbox h4 svg { width: 12px; height: 12px; fill: var(--green); }
  .avatar { width: 50px; height: 50px; border-radius: 50%; background: #c8eee0; margin: 9px auto 4px; }
  .newbox .name { font-size: 15px; }
  .newbox .age { font-size: 11px; margin-top: 1px; }
  .newbox .profil { display: block; color: var(--green); font-size: 14px; margin-top: 6px; }

  .search { left: 239px; top: 241px; width: 360px; height: 45px; border: 1px solid var(--line); display: flex; align-items: center; gap: 12px; padding-left: 16px; font-size: 15.5px; color: var(--ink-soft); }
  .search svg { width: 17px; height: 17px; }
  .searchbtn { left: 605px; top: 242px; width: 115px; height: 43px; font-size: 16px; }
  .rule { left: 239px; top: 298px; width: 481px; border-top: 1px solid var(--line); }
  .hero { left: 239px; top: 319px; width: 481px; height: 290px; background: radial-gradient(ellipse at 50% 55%, #e9f0ee, #c9d6d2); }
  .welcome { left: 239px; top: 627px; width: 481px; height: 203px; background: var(--mint); padding: 22px 27px; }
  .welcome h1 { font-size: 37px; font-weight: 400; color: #3a5a52; letter-spacing: .2px; }
  .welcome p { margin-top: 17px; font-size: 14.5px; line-height: 18px; color: var(--ink); }
  .subjects { left: 243px; top: 848px; width: 480px; font-size: 13.5px; line-height: 22px; color: var(--ink-soft); }
  .subjects h2 { font-size: 14px; font-weight: 400; color: var(--green); margin-bottom: 5px; }
  .subjects a { color: var(--link); }
  .subjects i { font-style: normal; color: #e3c98a; margin: 0 5px; }

  .right { left: 760px; width: 180px; }
  .right h3 { display: flex; align-items: center; gap: 9px; font-size: 16px; font-weight: 400; color: var(--green); }
  .right h3 svg { width: 12px; height: 12px; fill: var(--green); }
  .right p { font-size: 14.5px; line-height: 18px; margin-top: 10px; }
  .right .links { font-size: 14px; color: var(--link); margin-top: 8px; }
  .right .links i { color: var(--mint-border); font-style: normal; margin: 0 4px; }
  .nomsg { margin-top: 7px; height: 34px; font-size: 14px; }
  .promo { left: 760px; top: 384px; width: 180px; height: 384px; background: linear-gradient(180deg, #8ccab5, #6fbaa0); padding: 184px 11px 0; color: #fff; }
  .promo .small { font-size: 17px; line-height: 21px; font-weight: 300; }
  .promo .big { font-size: 40px; line-height: 40px; font-weight: 300; margin-top: 4px; }
  .promo .reg { margin-top: 20px; width: 153px; height: 32px; background: var(--green-deep); color: #fff; font-size: 14px; font-weight: 500; display: flex; align-items: center; justify-content: center; }
  .online { left: 760px; top: 768px; width: 180px; height: 35px; background: #c5eee0; display: flex; align-items: center; gap: 8px; padding-left: 9px; font-size: 14.5px; color: var(--ink); }
  .online svg { width: 12px; height: 12px; fill: var(--ink); }

  .footer { left: 20px; right: 20px; top: 1030px; border-top: 1px solid var(--line); padding-top: 15px; display: flex; justify-content: space-between; font-size: 13px; }
  .footer .copy { color: var(--muted); }
  .footer nav { color: #222; margin-right: -5px; }
</style>
</head>
<body>
<div class="page">
  <header>
    <a class="abs brand" href="#">Kreidetafel.de</a>
    <div class="abs field" style="left:551px"><svg viewBox="0 0 12 12"><circle cx="6" cy="3.5" r="3"/><path d="M0 12c0-4 3-5 6-5s6 1 6 5z"/></svg>Username</div>
    <div class="abs field" style="left:707px"><svg viewBox="0 0 12 12"><rect x="1" y="5" width="10" height="7"/><path d="M3 5V3.5a3 3 0 016 0V5H7.5V3.5a1.5 1.5 0 00-3 0V5z"/></svg>Passwort</div>
    <a class="abs btn login" href="#">Login</a>

    <nav class="abs mainnav">
      <a href="#"><svg viewBox="0 0 12 12"><path d="M6 0l6 6h-2v6H7V8H5v4H2V6H0z"/></svg>STARTSEITE</a>
      <a href="#" style="margin-left:40px"><svg viewBox="0 0 12 12"><circle cx="3" cy="2" r="1.7"/><circle cx="9" cy="2" r="1.7"/><rect x="1.5" y="4.5" width="3" height="7.5"/><rect x="7.5" y="4.5" width="3" height="7.5"/></svg>COMMUNITY</a>
      <a href="#" style="margin-left:41px"><svg viewBox="0 0 12 12"><path d="M6 0l6 3.5L6 7 0 3.5z"/><path d="M1.5 6L6 8.6 10.5 6 12 7 6 10.5 0 7z"/></svg>REFERATE</a>
      <a href="#" style="margin-left:auto"><svg viewBox="0 0 12 12"><path d="M0 0h10v7H3l-3 3zM11 3h1v9l-2-2H3V9h8z"/></svg>FOREN</a>
      <a href="#" style="margin-left:41px"><svg viewBox="0 0 12 12"><circle cx="4" cy="3" r="2.2"/><circle cx="9" cy="3.5" r="1.8"/><path d="M0 11c0-3 2-4 4-4s4 1 4 4zM8.5 11c0-2-.5-3-1.5-3.6 3-1 5 .6 5 3.6z"/></svg>MITGLIEDER</a>
      <a href="#" style="margin-left:41px"><svg viewBox="0 0 12 12"><path d="M5 0a5 5 0 014 8l3 3-1 1-3-3A5 5 0 115 0zm0 2a3 3 0 100 6 3 3 0 000-6z"/></svg>FLIRTSUCHE</a>
    </nav>
    <div class="abs crumbs">Foren<i>|</i>Mitglieder<i>|</i>Flirtsuche</div>
  </header>

  <aside class="abs side" style="top:226px">
    <h3><svg viewBox="0 0 12 12"><circle cx="3" cy="2" r="1.7"/><circle cx="9" cy="2" r="1.7"/><rect x="1.5" y="4.5" width="3" height="7.5"/><rect x="7.5" y="4.5" width="3" height="7.5"/></svg>Community</h3>
    <ul class="menu" style="margin-top:6px">
      <li><svg viewBox="0 0 12 12"><circle cx="7" cy="3" r="2.5"/><path d="M2 12c0-4 2.5-5 5-5s5 1 5 5zM0 4h4v1.5H0zM1.25 2.75h1.5v4h-1.5z"/></svg>Registrieren</li>
      <li><svg viewBox="0 0 12 12"><circle cx="4" cy="3" r="2.2"/><circle cx="9" cy="3.5" r="1.8"/><path d="M0 11c0-3 2-4 4-4s4 1 4 4zM8.5 11c0-2-.5-3-1.5-3.6 3-1 5 .6 5 3.6z"/></svg>Mitglieder Login</li>
      <li><svg viewBox="0 0 12 12"><path d="M0 2h7v8H0zm1 1v2h5V3zm0 3v3h5V6zM8 2h1.5v8H8zm2.5 0H12v8h-1.5z"/></svg>Foren</li>
      <li><svg viewBox="0 0 12 12"><path d="M0 0h12v9H3l-3 3zm2 2v1h8V2zm0 3v1h6V5z"/></svg>Chat</li>
      <li><svg viewBox="0 0 12 12"><path d="M5 0a5 5 0 014 8l3 3-1 1-3-3A5 5 0 115 0zm0 2a3 3 0 100 6 3 3 0 000-6z"/></svg>Flirtsuche</li>
    </ul>

    <h3 style="margin-top:29px"><svg viewBox="0 0 12 12"><path d="M6 0l6 3.5L6 7 0 3.5z"/><path d="M1.5 6L6 8.6 10.5 6 12 7 6 10.5 0 7z"/></svg>Schule &amp; Uni</h3>
    <ul class="menu" style="margin-top:6px">
      <li><svg viewBox="0 0 12 12"><path d="M0 0h12v12H0zm6 2.5a2 2 0 100 4 2 2 0 000-4zM2.5 10h7c0-2-1.5-3-3.5-3s-3.5 1-3.5 3z"/></svg>Hausarbeit</li>
      <li><svg viewBox="0 0 12 12"><path d="M0 0h12v12H0zm1.3 1.3v9.4h9.4V1.3zM6 3a1.7 1.7 0 110 3.4A1.7 1.7 0 016 3zM3 9.5c0-1.6 1.3-2.4 3-2.4s3 .8 3 2.4z"/></svg>Referat</li>
    </ul>

    <h3 style="margin-top:36px"><svg viewBox="0 0 12 12"><path d="M0 0h12v12H0zm2 6v4h1.6V6zm3.2-3v7h1.6V3zm3.2 4.5V10H10V7.5z"/></svg>Statistik</h3>
    <ul class="stats" style="margin-top:4px">
      <li><span>Mitglieder</span><span>401.324</span></li>
      <li><span>Männer</span><span>197.694</span></li>
      <li><span>Frauen</span><span>196.799</span></li>
      <li><span>Referate</span><span>12.458</span></li>
      <li><span>Forenbeiträge</span><span>3M+</span></li>
    </ul>
  </aside>

  <section class="abs newbox">
    <h4><svg viewBox="0 0 12 12"><circle cx="7" cy="3" r="2.5"/><path d="M2 12c0-4 2.5-5 5-5s5 1 5 5zM0 4h4v1.5H0zM1.25 2.75h1.5v4h-1.5z"/></svg>Neue Mitglieder</h4>
    <div class="avatar" role="img" aria-label="Profilbild-Platzhalter"></div>
    <div class="name">Lernfuchs</div>
    <div class="age">Alter: 60 Jahre</div>
    <a class="profil" href="#">Profil</a>
  </section>

  <main>
    <div class="abs search"><svg viewBox="0 0 17 17" fill="none" stroke="#a9b5b2" stroke-width="1.8"><circle cx="7" cy="7" r="5.5"/><path d="M11 11l5 5"/></svg>Was suchst du? Hier eingeben!</div>
    <a class="abs btn searchbtn" href="#">Suchen</a>
    <div class="abs rule"></div>
    <div class="abs hero" role="img" aria-label="Illustration: Schüler mit Brille sitzt lesend zwischen Bücherstapeln"></div>
    <section class="abs welcome">
      <h1>Hallo Besucher,</h1>
      <p>Auf Kreidetafel.de findest du viele Referate, Facharbeiten und Hausaufgaben. Solltest du einmal ein Referat zu einem Thema nicht finden, kannst du deine Frage bei uns im Forum stellen, wo dir in der Regel schnell geholfen wird.</p>
    </section>
    <section class="abs subjects">
      <h2>Referate - Hausarbeiten - Hausaufgaben zu folgenden Fächern:</h2>
      <a href="#">Deutsch</a> (2937)<i>|</i><a href="#">Englisch</a> (1113)<i>|</i><a href="#">Latein</a> (275)<i>|</i><a href="#">Franzoesisch</a> (196)<br>
      <a href="#">|Italienisch</a> (32)<i>|</i><a href="#">Griechisch</a> (28)<i>|</i><a href="#">Spanisch</a> (74)<i>|</i><a href="#">Mathematik</a> (99)<br>
      <i style="margin-left:0">|</i><a href="#">Physik</a> (481)<i>|</i><a href="#">Chemie</a> (450)<i>|</i><a href="#">Astronomie</a> (82)<i>|</i><a href="#">Geographie</a> (785)<br>
      <i style="margin-left:0">|</i><a href="#">Geschichte</a> (1870)<i>|</i><a href="#">Sozialkunde</a> (555)<i>|</i><a href="#">Wirtschaft</a> (435) <a href="#">|Recht</a><br>
      (109)<i>|</i><a href="#">Musik</a> (448)<i>|</i><a href="#">Kunst</a> (265)<i>|</i><a href="#">Religion</a> (521)<i>|</i><a href="#">Informatik</a> (191)<i>|</i><br>
      <a href="#">Hauswirtschaft</a> (109)<i>|</i><a href="#">Sport</a> (136)<i>|</i><a href="#">Chor</a> (19)<i>|</i><a href="#">Biologie</a> (1237)
    </section>
  </main>

  <aside class="abs right" style="top:227px">
    <h3><svg viewBox="0 0 12 12"><path d="M0 0h10v7H3l-3 3zM11 3h1v9l-2-2H3V9h8z"/></svg>LiveMessenger</h3>
    <p>Diese Funktion ist nur für Mitglieder verfügbar</p>
    <div class="links">Mitglieder<i>|</i>Flirtsuche</div>
    <div class="btn nomsg">Keine neue Nachricht</div>
  </aside>
  <section class="abs promo" role="img" aria-label="Foto: Lernende in einer Bibliothek, grün eingefärbt">
    <div class="small">Dein<br>kreidetafel.de</div>
    <div class="big">Schon dabei?</div>
    <a class="reg" href="#">Registrieren</a>
  </section>
  <div class="abs online"><svg viewBox="0 0 12 12"><circle cx="4" cy="3" r="2.2"/><circle cx="9" cy="3.5" r="1.8"/><path d="M0 11c0-3 2-4 4-4s4 1 4 4zM8.5 11c0-2-.5-3-1.5-3.6 3-1 5 .6 5 3.6z"/></svg>204 Mitglieder online</div>

  <footer class="abs footer">
    <span class="copy">© 2017 kreidetafel.de</span>
    <nav>Hauptseite | Referate Schule - Hausarbeit | Impressum | Datenschutz | AGB</nav>
  </footer>
</div>
</body>
</html>
```